Visitenkarten-Design für Garten- und Landschaftspflege
Karvan Meltis setzte meine Vorstellungen absolut super um ich kann Ihn nur weiter empfehlen. vielen dank
Zielgruppe
Baumpflege, Baumfällung, Garten und Landschaftspflege meine zielgruppe sind Privatpersonen im alter von 20-100Jahren
Aufgabenstellung
Sehr geehrte Damen und Herren, die visitenkarte sollte die angaben so enthalten wie sie auf der von mir gestallteten Visitenkarten sind ( meine ist kein maß der Dinge). Ich habe mein Logo leider nur als 3.jpg Datei. Das Logo darf im Design erändert werden aber bitte nur Feinheiten ansonsten stehen ihnen alle türen offen um kreativ zu sein.
mit freundlichen Grüßen Jonas Wendtholm

```html
<!DOCTYPE html>
<html lang="de">
<head>
<meta charset="utf-8">
<title>Visitenkarte Baumpflege Wendtholm</title>
<link rel="stylesheet" href="https://fonts.googleapis.com/css2?family=Barlow:wght@400;500;600&display=swap">
<style>
  :root {
    --page: #ffffff;
    --card: #ffffff;
    --ink: #111111;
    --accent-red: #b5373a;
    --leaf-green: #a3c040;
    --band: #0c0c0c;
    --edge: #c9c9c9;
    --tree-dark: #1a1a1a;
    --tree-mid: #3a3a3a;
  }
  * { margin: 0; padding: 0; box-sizing: border-box; }
  html, body {
    width: 925px; height: 1200px; overflow: hidden;
    background: var(--page);
    font-family: "Barlow", Arial, sans-serif;
    color: var(--ink);
  }
  .card {
    position: absolute; left: 122px; width: 672px; height: 436px;
    background: var(--card);
    border: 1px solid var(--edge);
    box-shadow: 10px 14px 16px rgba(0,0,0,0.28);
    overflow: hidden;
  }
  .card--front { top: 88px; }
  .card--back { top: 647px; }

  .tree-illustration {
    position: absolute;
    background: radial-gradient(ellipse at 50% 40%, var(--tree-mid) 0%, var(--tree-dark) 60%, rgba(26,26,26,0.85) 100%);
    border-radius: 45% 45% 8% 8%;
  }
  .card--front .tree-illustration { left: 25px; top: 35px; width: 316px; height: 213px; }
  .card--back .tree-illustration { left: 372px; top: 15px; width: 268px; height: 136px; }

  .holder-name {
    position: absolute; right: 34px; top: 52px;
    font-size: 34px; font-weight: 500; color: var(--accent-red);
  }
  .holder-title {
    position: absolute; right: 34px; top: 112px;
    text-align: right; font-size: 20px; line-height: 26px; font-weight: 400;
  }

  .ground-line {
    position: absolute; left: 0; width: 100%; height: 6px; background: var(--band);
  }
  .card--front .ground-line { top: 248px; }
  .card--back .ground-line { top: 151px; }

  .brand-band {
    position: absolute; left: 35px; top: 254px; width: 599px; height: 62px;
    background: var(--band);
    display: flex; align-items: center; justify-content: center;
  }
  .brand-name {
    color: #ffffff; font-size: 40px; font-weight: 600; letter-spacing: 1px;
    text-transform: uppercase; white-space: nowrap;
  }

  .green-panel {
    position: absolute; left: 0; bottom: 0; width: 100%;
    background: var(--leaf-green);
  }
  .card--front .green-panel { top: 316px; }
  .card--back .green-panel { top: 157px; }

  .contact-line {
    position: absolute; left: 0; width: 100%;
    text-align: center; font-size: 21px; white-space: nowrap;
  }
  .contact-line--address { top: 18px; }
  .contact-line--web { top: 52px; }

  .services-title {
    position: absolute; left: 29px; top: 62px;
    font-size: 34px; font-weight: 500; color: var(--accent-red);
  }
  .services-list {
    position: absolute; left: 24px; top: 16px;
    list-style: none; font-size: 23px; line-height: 37px;
  }
  .services-list li::before { content: "\2022\00a0"; }
</style>
</head>
<body>

<section class="card card--front">
  <div class="tree-illustration" role="img" aria-label="Silhouette eines großen Laubbaums zwischen zwei Holzzäunen auf einem Hügel"></div>
  <h1 class="holder-name">Jonas Wendtholm</h1>
  <p class="holder-title">Fachagrarwirt<br>Baumpflege und<br>Baumsanierung</p>
  <div class="ground-line"></div>
  <div class="brand-band"><span class="brand-name">Baumpflege Wendtholm</span></div>
  <div class="green-panel">
    <p class="contact-line contact-line--address">Lindenweg 4 • 85614 Kirchstetten &nbsp;• &nbsp;Tel. 0171 482 59 30</p>
    <p class="contact-line contact-line--web">kontakt@baumpflege-wendtholm.de • baumpflege-wendtholm.de</p>
  </div>
</section>

<section class="card card--back">
  <h2 class="services-title">Unsere Leistungen</h2>
  <div class="tree-illustration" role="img" aria-label="Kleine Silhouette eines Laubbaums zwischen zwei Holzzäunen"></div>
  <div class="ground-line"></div>
  <div class="green-panel">
    <ul class="services-list">
      <li>Neu-Pflanzungen</li>
      <li>Herstellen der Verkehrssicherheit von Bäumen</li>
      <li>Kronenrückschnitt (Einkürzung und Kronenpflege)</li>
      <li>Prüfen von Bäumen auf Standsicherheit</li>
      <li>Fräsen von Wurzelstöcken</li>
      <li>Anbau und Fertigung von Gartenhäusern nach Maß</li>
    </ul>
  </div>
</section>

</body>
</html>
```